Online Rug Store needs Clearance Banner

Website is: Marvelous Mats and Interiors
You can access it at: www.marvelousmatsandinteriors-example.com and login (top right) with password: plorvat

*** update: When creating banners for my site, you have permission to use images from www.kelvora-example.com, but ONLY for this project. The images/artwork are copyright allowable for use on www.marvelousmatsandinteriors-example.com projects.***

We need a home page banner sized 1000 wide x 500 tall pixels to promote a "Clearance Sale" on rugs. The banner can state:

1. Clearance Sale
2. Now in progress
3. Save an extra 20% with coupon code 'Take20'
4. Ends March 31st
5. Plus Free Shipping and 30 day returns.

We prefer a banner that appears hand-drawn and artistic, not commercially produced. It is OK to use a room scene image, rug images, or just a colored/textured background with text and no images. Your choice.

Flat graphics with no shadows and 3-D effect preferred.
Attached is are 3 logo options, as well as an example banner with handcrafted, artistic styling that we prefer.

Target Market(s)

This should be an eye-catching banner to showcase a very urgent promotion. Consider using colors of red, white, gold, and black to make a strong statement on the home page.

Industry/Entity Type

Home And Garden

Requirements
Must have
• Winner must provide Photoshop editable file format (.psd format) including layers that can be edited.
Nice to have
• Hand-drawn, stenciled, scribbled, artistic graphics and fonts is nice because we sell rugs that are made by hand.
Should not have
• little to no shadowing. Avoid computerized graphics.

```html
<!DOCTYPE html>
<html lang="en">
<head>
<meta charset="utf-8">
<title>Marvelous Mats and Interiors – Clearance Sale</title>
<link href="https://fonts.googleapis.com/css2?family=Cinzel&family=Josefin+Sans:wght@400;600;700&display=swap" rel="stylesheet">
<style>
  :root {
    --room-light: #e9ecef;
    --room-mid: #c9c9c6;
    --room-green: #9aa590;
    --bed-red: #c4646a;
    --panel: rgba(255,255,255,0.62);
    --coral: #ef5f4c;
    --ink: #333333;
    --slate: #3f5268;
    --brand: #2f2f2f;
    --white: #ffffff;
  }
  html, body { margin: 0; padding: 0; overflow: hidden; }
  body { width: 1200px; height: 600px; background: var(--white); }
  .banner {
    position: relative; width: 1200px; height: 600px; overflow: hidden;
    font-family: "Josefin Sans", sans-serif;
  }
  .room-photo {
    position: absolute; inset: 0;
    background:
      radial-gradient(ellipse 420px 200px at 560px 470px, var(--bed-red) 0%, rgba(196,100,106,0.5) 60%, transparent 100%),
      linear-gradient(180deg, var(--room-green) 0%, var(--room-light) 45%, var(--room-mid) 100%);
  }
  .panel {
    position: absolute; left: 67px; top: 36px; width: 1066px; height: 528px;
    background: var(--panel);
  }
  .brand {
    position: absolute; top: 62px; left: 0; right: 0;
    display: flex; justify-content: center; align-items: center; gap: 14px;
  }
  .brand-mark { width: 70px; height: 70px; background: var(--coral); }
  .brand-name {
    font-family: "Cinzel", serif; font-size: 30px; color: var(--brand);
    line-height: 1.15; text-align: left;
  }
  .line { position: absolute; left: 0; right: 0; text-align: center; margin: 0; text-transform: uppercase; }
  .headline { top: 150px; font-size: 50px; font-weight: 700; letter-spacing: 14px; color: var(--coral); }
  .status { top: 215px; font-size: 36px; font-weight: 600; letter-spacing: 7px; color: var(--ink); }
  .offer { top: 258px; font-size: 44px; font-weight: 700; letter-spacing: 9px; color: var(--ink); }
  .discount-row {
    position: absolute; top: 325px; left: 0; right: 0;
    display: flex; justify-content: center; align-items: center; gap: 50px;
  }
  .discount { font-size: 56px; font-weight: 700; color: #4a5160; letter-spacing: 3px; }
  .coupon {
    background: var(--coral); color: var(--white); padding: 4px 12px 6px; text-align: center;
  }
  .coupon-label { display: block; font-size: 15px; letter-spacing: 2px; }
  .coupon-code { display: block; font-size: 28px; font-weight: 700; letter-spacing: 2px; }
  .deadline { top: 405px; font-size: 40px; font-weight: 400; letter-spacing: 2px; color: var(--ink); }
  .perks {
    top: 460px; font-size: 40px; font-weight: 700; letter-spacing: 9px;
    line-height: 1.2; color: var(--slate);
  }
</style>
</head>
<body>
  <div class="banner">
    <div class="room-photo" role="img" aria-label="Bright modern bedroom with a round red bed, white chairs and large windows overlooking trees"></div>
    <div class="panel"></div>
    <div class="brand">
      <span class="brand-mark"></span>
      <span class="brand-name">Marvelous Mats<br>and Interiors</span>
    </div>
    <h1 class="line headline">Clearance Sale</h1>
    <p class="line status">Now in Progress</p>
    <p class="line offer">Save an Extra</p>
    <div class="discount-row">
      <span class="discount">20%</span>
      <span class="coupon"><span class="coupon-label">COUPON CODE</span><span class="coupon-code">Take20</span></span>
    </div>
    <p class="line deadline">Ends March 31st</p>
    <p class="line perks">Plus Free Shipping<br>and 30 Day Returns</p>
  </div>
</body>
</html>
```